Restaurant service company needs a website!

I am looking for a skilled web designer/developer to create a professional, responsive, and easy-to-navigate website for my company, which specializes in servicing restaurant cooking equipment. The site should communicate trust, reliability, and technical expertise to our target audience, restaurant owners, managers, and commercial kitchen operators. I have included the company logos, if any other format for them is needed please let me know.

Target Market(s)

restaurant owners, managers, and commercial kitchen operators

Industry/Entity Type

Commercial Kitchen Equipment Service

Coding

Coded - Design and coding required

Number of Pages Required

1 page

Font styles to use
Serif
Sans Serif

Requirements
Must have
• Contact and service request forms, Click-to-call functionality for mobile, Clean, modern layout with strong visuals, Easy navigation, mobile-friendly
Nice to have
• Testimonials or Reviews, If possible a click-to-text functionality for mobile.
Should not have
• Any mention of Refrigeration or HVAC, "Free Quotes"

```html
<!DOCTYPE html>
<html lang="en">
<head>
<meta charset="utf-8">
<title>Waypoint Kitchen Service</title>
<link href="https://fonts.googleapis.com/css2?family=Outfit:wght@400;500;600;700&display=swap" rel="stylesheet">
<style>
:root{
  --teal:#0e6a80;
  --teal-deep:#0b5466;
  --ink:#0d2f3a;
  --text:#3d4b52;
  --night:#0a3a47;
  --mist:#e3edf0;
  --white:#ffffff;
}
*{box-sizing:border-box;margin:0;padding:0}
html,body{width:1200px;height:3693px;overflow:hidden}
body{position:relative;font-family:'Outfit',sans-serif;color:var(--text);background:var(--white)}
.abs{position:absolute}
.btn{position:absolute;display:flex;align-items:center;justify-content:center;background:var(--teal);color:#fff;font-weight:600;font-size:12px;border-radius:3px;text-decoration:none}
.btn-outline{background:#fff;color:var(--ink);border:1.5px solid var(--ink)}
h1,h2,h3{color:var(--ink);font-weight:700}

/* header */
.site-header{left:0;top:0;width:1200px;height:73px;background:#fff}
.brand{display:flex;align-items:center;gap:8px;left:93px;top:18px}
.brand-square{width:22px;height:22px;border:2.5px solid var(--teal);border-radius:3px}
.brand-name{font-weight:700;font-size:20px;color:var(--teal);letter-spacing:.3px}
.main-nav{left:536px;top:29px;display:flex;gap:25px;font-size:12.5px;color:var(--ink)}
.main-nav a{color:inherit;text-decoration:none}

/* hero */
.hero{left:0;top:73px;width:1200px;height:605px;background:linear-gradient(90deg,#e6ecee 0%,#dde5e8 40%,#b6c3c7 65%,#7f8e93 100%)}
.hero-title{left:95px;top:190px;font-size:39px;line-height:42px;width:520px}
.hero-text{left:96px;top:330px;width:420px;font-size:12.5px;line-height:19px}
.side-tab{left:1117px;top:182px;width:47px;height:184px;background:#fff;border-radius:6px 0 0 6px;box-shadow:0 2px 8px rgba(0,0,0,.15);display:flex;align-items:center;justify-content:center}
.side-tab span{transform:rotate(-90deg);white-space:nowrap;font-size:11px;font-weight:600;color:var(--ink)}
.chat-btn{left:1117px;top:376px;width:47px;height:48px;background:var(--teal);border-radius:6px 0 0 6px}
.scroll-bump{left:540px;top:640px;width:120px;height:60px;background:#fff;border-radius:60px 60px 0 0}

/* about */
.about-photo{left:328px;top:797px;width:313px;height:432px;border-radius:22px;background:linear-gradient(160deg,#8d9499,#4c5358 60%,#2b3034)}
.values-card{left:136px;top:843px;width:258px;height:341px;border-radius:14px;background:var(--teal);border:3px solid #fff;padding:46px 0 0 38px}
.value{display:flex;gap:18px;margin-bottom:26px}
.value-icon{width:44px;height:44px;border-radius:6px;background:rgba(255,255,255,.35);flex:none}
.value h4{color:#fff;font-size:11.5px;font-weight:700;margin:8px 0 6px}
.value p{color:#e2f0f3;font-size:10px;line-height:15px;width:130px}
.about-title{left:708px;top:893px;font-size:30px;line-height:33px}
.about-text{left:708px;top:978px;width:330px;font-size:12px;line-height:18.7px}

/* services */
.section-title{left:0;width:1200px;text-align:center;font-size:30px}
.section-sub{left:0;width:1200px;text-align:center;font-size:12.5px}
.service{width:207px;top:1408px}
.service-photo{width:207px;height:262px;border-radius:14px;background:linear-gradient(170deg,#b9bec0,#6c7275 55%,#34393c)}
.service-num{position:absolute;top:20px;right:20px;width:44px;height:42px;border:2px solid #fff;border-radius:8px;color:#fff;font-size:19px;font-weight:600;display:flex;align-items:center;justify-content:center}
.service-label{display:flex;justify-content:space-between;align-items:center;padding:20px 18px 0 21px}
.service-label h3{font-size:19px;line-height:25px;font-weight:600}
.divider{left:110px;top:1803px;width:980px;height:1px;background:#e7ecee}

/* industries */
.industries-bg{left:0;top:1821px;width:1200px;height:416px;background:linear-gradient(180deg,#fff,#f1f5f6)}
.industry-card{left:161px;top:1966px;width:879px;height:426px;border-radius:44px;background:var(--mist);border:6px solid #fff;box-shadow:0 6px 24px rgba(0,0,0,.12)}
.industry-photo{left:647px;top:1989px;width:370px;height:380px;border-radius:28px;background:linear-gradient(150deg,#cfc9c0,#7d7165 50%,#3f3a35)}
.industry-title{left:250px;top:2092px;font-size:19px;font-weight:600}
.industry-text{left:250px;top:2132px;width:320px;font-size:12px;line-height:18.5px}

/* testimonials */
.testimonials{left:0;top:2286px;width:1200px;height:667px;background:linear-gradient(180deg,#0c4a5a,var(--night) 60%,#082f3a)}
.brand-tile{left:129px;top:2521px;width:301px;height:301px;border-radius:26px;background:#1a7d93;display:flex;align-items:center;justify-content:center;gap:12px}
.brand-tile span{color:#fff;font-weight:700;font-size:22px}
.brand-tile i{width:26px;height:26px;border:3px solid #fff;border-radius:4px}
.testi-title{left:505px;top:2583px;font-size:29px;color:#fff}
.testi-quote{left:505px;top:2640px;width:580px;font-size:21px;line-height:30px;font-style:italic;font-weight:400;color:#e8f1f3}
.testi-author{left:505px;top:2734px;font-size:13px;font-weight:600;color:#fff;text-decoration:underline}

/* cta */
.cta-title{left:0;width:1200px;top:3068px;text-align:center;font-size:31px;font-weight:600}
.cta-sub{left:0;width:1200px;top:3113px;text-align:center;font-size:13px;color:var(--ink)}

/* footer */
.site-footer{left:0;top:3298px;width:1200px;height:395px;background:var(--teal)}
.foot-brand{left:110px;top:3455px;width:142px;text-align:center;color:#fff}
.foot-brand b{display:block;font-size:19px;line-height:22px}
.foot-brand small{font-size:9px;letter-spacing:3px}
.foot-square{left:161px;top:3400px;width:40px;height:40px;border:3px solid #fff;border-radius:4px}
.social{top:3546px;width:31px;height:31px;border-radius:50%;background:rgba(255,255,255,.18)}
.vline{top:3384px;width:1px;height:213px;background:rgba(255,255,255,.3)}
.foot-col{top:3428px;color:#fff}
.foot-col h5{font-size:15px;font-weight:600;margin-bottom:17px}
.foot-col li{list-style:none;font-size:11.5px;line-height:20px}
.copyright{left:0;width:1200px;top:3655px;text-align:center;color:#fff;font-size:11.5px}
.to-top{left:1137px;top:3642px;width:32px;height:32px;border-radius:50%;background:#fff}
</style>
</head>
<body>

<header class="abs site-header">
  <div class="abs brand"><div class="brand-square"></div><span class="brand-name">WAYPOINT</span></div>
  <nav class="abs main-nav">
    <svg width="12" height="12" viewBox="0 0 12 12"><path d="M1 6 6 1l5 5H9.5v5h-2.5V8h-2v3H2.5V6z" fill="#0e6a80"/></svg>
    <a>About Us</a><a>Services</a><a>Industries Served</a><a>Testimonials</a><a>Contact</a>
  </nav>
  <a class="btn" style="left:985px;top:21px;width:121px;height:32px">Request Service</a>
</header>

<section class="abs hero" role="img" aria-label="Chefs working at stainless steel cooking stations in a commercial kitchen"></section>
<h1 class="abs hero-title">RELIABLE SERVICE FOR YOUR RESTAURANT COOKING EQUIPMENT</h1>
<p class="abs hero-text">We keep your commercial kitchen running smoothly with trusted repairs, expert maintenance, and fast response times.</p>
<a class="btn" style="left:96px;top:456px;width:158px;height:33px">Request Service Now</a>
<div class="abs side-tab"><span>REQUEST A SERVICE VISIT</span></div>
<div class="abs chat-btn">
  <svg width="47" height="48" viewBox="0 0 47 48"><circle cx="23.5" cy="23" r="10" fill="none" stroke="#fff" stroke-width="2"/><path d="M20 21h7M20 25h5" stroke="#fff" stroke-width="2"/></svg>
</div>
<div class="abs scroll-bump"></div>
<svg class="abs" style="left:583px;top:661px" width="34" height="34" viewBox="0 0 34 34"><circle cx="17" cy="17" r="15.5" fill="none" stroke="#0d2f3a" stroke-width="1.6"/><path d="M17 9v15M11.5 18.5 17 24l5.5-5.5" fill="none" stroke="#0d2f3a" stroke-width="1.6"/></svg>

<div class="abs about-photo" role="img" aria-label="Technician servicing a commercial oven"></div>
<div class="abs values-card">
  <div class="value"><div class="value-icon"></div><div><h4>RELIABILITY</h4><p>We respond quickly and get the job done right.</p></div></div>
  <div class="value"><div class="value-icon"></div><div><h4>EXPERTISE</h4><p>Skilled technicians with hands-on industry knowledge.</p></div></div>
  <div class="value"><div class="value-icon"></div><div><h4>TRUST</h4><p>Clear communication, honest pricing, and dependable results.</p></div></div>
</div>
<h2 class="abs about-title">TRUSTED SERVICE.<br>PROVEN EXPERTISE.</h2>
<p class="abs about-text">For years, we've been helping restaurants and commercial kitchens keep their equipment performing at its best. Our team of certified technicians specializes in servicing all major brands of cooking equipment. From emergency repairs to routine maintenance, we deliver professional service you can count on.</p>
<a class="btn" style="left:708px;top:1111px;width:160px;height:35px">Request Service Now</a>

<h2 class="abs section-title" style="top:1316px">WHAT WE DO BEST</h2>
<p class="abs section-sub" style="top:1366px">We provide complete service solutions for restaurant cooking equipment:</p>

<div class="abs service" style="left:161px">
  <div class="service-photo" role="img" aria-label="Chef cooking over a flaming range"></div><span class="service-num">01</span>
  <div class="service-label"><h3>EQUIPMENT<br>REPAIR</h3><svg width="22" height="14" viewBox="0 0 22 14"><path d="M0 7h20M14 1l6 6-6 6" fill="none" stroke="#0e6a80" stroke-width="1.8"/></svg></div>
</div>
<div class="abs service" style="left:384px">
  <div class="service-photo" role="img" aria-label="Cook checking equipment at a kitchen station"></div><span class="service-num">02</span>
  <div class="service-label"><h3>PREVENTIVE<br>MAINTENANCE</h3><svg width="22" height="14" viewBox="0 0 22 14"><path d="M0 7h20M14 1l6 6-6 6" fill="none" stroke="#0e6a80" stroke-width="1.8"/></svg></div>
</div>
<div class="abs service" style="left:608px">
  <div class="service-photo" role="img" aria-label="Kitchen manager on a phone call with a notepad"></div><span class="service-num">03</span>
  <div class="service-label"><h3>EMERGENCY<br>SERVICE</h3><svg width="22" height="14" viewBox="0 0 22 14"><path d="M0 7h20M14 1l6 6-6 6" fill="none" stroke="#0e6a80" stroke-width="1.8"/></svg></div>
</div>
<div class="abs service" style="left:830px">
  <div class="service-photo" role="img" aria-label="Staff arranging dishes on kitchen shelving"></div><span class="service-num">04</span>
  <div class="service-label"><h3>INSTALLATION<br>&amp; SETUP</h3><svg width="22" height="14" viewBox="0 0 22 14"><path d="M0 7h20M14 1l6 6-6 6" fill="none" stroke="#0e6a80" stroke-width="1.8"/></svg></div>
</div>

<div class="abs divider"></div>

<div class="abs industries-bg"></div>
<h2 class="abs section-title" style="top:1870px">INDUSTRIES WE SERVE</h2>
<p class="abs section-sub" style="top:1920px">Trusted by diverse foodservice businesses to keep kitchens running without interruptions.</p>

<section class="abs testimonials" role="img" aria-label="Dimmed restaurant dining room backdrop"></section>
<div class="abs industry-card"></div>
<div class="abs industry-photo" role="img" aria-label="Café owner talking with a customer"></div>
<h3 class="abs industry-title">RESTAURANTS &amp; CAFÉS</h3>
<p class="abs industry-text">From small cafés to large-scale restaurants, we understand the urgency of keeping your kitchen fully operational. Our team provides fast, reliable repair and preventive maintenance so you can focus on delivering great food and service to your customers.</p>
<a class="btn" style="left:250px;top:2247px;width:104px;height:33px">View detail</a>

<div class="abs brand-tile"><i></i><span>WAYPOINT</span></div>
<h2 class="abs testi-title">WHAT OUR CLIENTS SAY</h2>
<p class="abs testi-quote">"The team is always on time and gets the job done right. We trust them with all of our kitchen equipment."</p>
<p class="abs testi-author">RESTAURANT OWNER</p>
<svg class="abs" style="left:793px;top:2736px" width="48" height="16" viewBox="0 0 48 16"><path d="M14 8H1M6 3 1 8l5 5" fill="none" stroke="#fff" stroke-width="1.4"/><path d="M24 8h22M40 2l6 6-6 6" fill="none" stroke="#fff" stroke-width="1.8"/></svg>

<h2 class="abs cta-title">Need Immediate Service?</h2>
<p class="abs cta-sub">We're just a call or click away. Request a technician today and keep your kitchen running at full speed.</p>
<a class="btn" style="left:467px;top:3161px;width:128px;height:32px">Request Service</a>
<a class="btn btn-outline" style="left:604px;top:3161px;width:127px;height:32px">Call Us Today</a>

<footer class="abs site-footer"></footer>
<div class="abs foot-square"></div>
<div class="abs foot-brand"><b>WAYPOINT</b><small>KITCHEN SERVICE</small></div>
<div class="abs social" style="left:108px"></div>
<div class="abs social" style="left:150px"></div>
<div class="abs social" style="left:189px"></div>
<div class="abs social" style="left:225px"></div>
<div class="abs vline" style="left:326px"></div>
<div class="abs vline" style="left:561px"></div>
<div class="abs vline" style="left:869px"></div>
<div class="abs foot-col" style="left:400px"><h5>Quick Links</h5><ul><li>Home</li><li>About Us</li><li>Services</li><li>Contact</li></ul></div>
<div class="abs foot-col" style="left:635px"><h5>Business Hours</h5><ul><li>Mon–Fri: 8:00 AM – 8:00 PM</li><li>Sat: 9:00 AM – 5:00 PM</li><li>Emergency service available</li></ul></div>
<div class="abs foot-col" style="left:944px"><h5>What We Do Best</h5><ul><li>Equipment Repair</li><li>Preventive Maintenance</li><li>Emergency Service</li><li>Installation &amp; Setup</li></ul></div>
<p class="abs copyright">Copyright © 2025 Waypoint Kitchen Service. All Rights Reserved.</p>
<div class="abs to-top"><svg width="32" height="32" viewBox="0 0 32 32"><path d="M13 18l3-3 3 3" fill="none" stroke="#0d2f3a" stroke-width="1.6"/></svg></div>

</body>
</html>
```